A WEBSITE FOR A JEWELLERY RETAIL STORE WITH A SHOPPING CART, AND ABILITY TO ORDER ONLINE.

I require a website with a shopping cart.

We sell MAINLY diamond jewellery (such as rings etc). I need it to be simple to change prices with only a few buttons, as the price fluctuates due to the US Dollar.

We are a diamond wholesaler, selling directly to the public, so we guarantee the lowest prices in Australia.

There is also a link to current inventory that will need to be uploaded to the site.

This could be an ongoing job, where you will be paid weekly to maintain and update the website if you wish.

Target Market(s)

People getting engaged, and wanting to buy a diamond ring.

Number of Pages Required

5+ page

Colors

Designer to choose colors to be used in the design.

Requirements
Must have
• elegant.
• modern.
• professional.
• SHOPPING CART.
• ABILITY TO SEARCH FOR LOOSE DIAMONDS (LINK THAT NEEDS TO BE EMBEDDED WILL BE SENT WHICH SHOWS CURRENT STOCK).
• ENGAGEMENT RINGS
• WEDDING RINGS
• DIAMOND EARRINGS
• DIAMOND PENDANTS
• LOOSE DIAMONDS.
• SALE ITEMS.
• OTHER JEWELLERY.
• EDUCATION
• WISH LIST
• CART.
Nice to have
• a good place to look for inspiration on pages is https://www.velmarigems.example.
• YOU MAY VISIT OUR FACEBOOK PAGE AT.
• HTTP://WWW.SOCIALPAGE.EXAMPLE/QUINTORAJEWELLERS
Should not have
• We don't want it too busy.

```html
<!DOCTYPE html>
<html lang="en">
<head>
<meta charset="utf-8">
<title>Quintora Jewellers</title>
<link rel="stylesheet" href="https://fonts.googleapis.com/css2?family=Questrial&display=swap">
<style>
:root{
  --ink:#111111;
  --black:#000000;
  --paper:#ffffff;
  --muted:#555555;
  --rule:#9a9a9a;
  --tile:#000000;
  --gold:#f0b323;
  --hero-a:#3a3a3a;
  --hero-b:#050505;
  --gem-a:#d9d9d9;
  --gem-b:#4a4a4a;
  --ring-a:#f2f2f2;
  --ring-b:#c9c9c9;
  --frame:#bfbfbf;
}
*{margin:0;padding:0;box-sizing:border-box}
html,body{width:1200px;height:3010px;overflow:hidden;background:var(--paper)}
body{font-family:"Questrial",Arial,sans-serif;color:var(--ink);position:relative}
.abs{position:absolute}
a{color:inherit;text-decoration:none}

/* header */
.brand{left:38px;top:28px;display:flex;align-items:center;gap:10px}
.brand-mark{width:26px;height:26px;background:var(--ink)}
.brand-name{font-size:26px;letter-spacing:1px;line-height:1}
.brand-name small{display:block;font-size:12px;letter-spacing:6px;margin-top:3px}
.header-icons{right:44px;top:44px;display:flex;gap:30px}
.header-icons svg{width:18px;height:18px}
.main-nav{left:38px;top:92px;width:1118px;display:flex;justify-content:space-between;font-size:15px;letter-spacing:1.5px}

/* hero */
.hero{left:38px;top:132px;width:1118px;height:574px;background:radial-gradient(ellipse at 62% 35%,var(--hero-a),var(--hero-b) 70%)}
.hero-gems{left:492px;top:228px;width:580px;height:330px;border-radius:40% 40% 10% 10%;background:radial-gradient(ellipse at 50% 50%,var(--gem-a),var(--gem-b) 55%,transparent 75%);opacity:.8}
.hero-frame{left:72px;top:144px;width:428px;height:140px;border-top:1px solid var(--frame);border-left:1px solid var(--frame)}
.hero-frame::before{content:"";position:absolute;left:0;bottom:0;width:94px;border-bottom:1px solid var(--frame)}
.hero-frame::after{content:"";position:absolute;right:0;top:0;height:84px;border-right:1px solid var(--frame)}
.hero-title{left:92px;top:154px;color:var(--paper);line-height:1.14}
.hero-title .kicker{font-size:27px;letter-spacing:1px}
.hero-title .big{font-size:44px;letter-spacing:2px}
.hero-title .amp{font-size:44px;letter-spacing:2px;padding-left:98px}
.hero-title .amp span{font-size:28px}
.btn-outline{border:1px solid var(--paper);color:var(--paper);font-size:14px;display:flex;align-items:center;justify-content:center;letter-spacing:.5px}
.hero .btn-outline{left:72px;top:320px;width:156px;height:48px}
.dots{display:flex;gap:8px;align-items:center}
.dots i{width:9px;height:9px;border:1px solid currentColor;transform:rotate(45deg)}
.dots i.on{background:currentColor;width:11px;height:11px}
.hero .dots{left:92px;top:516px;color:var(--paper)}

/* categories */
.categories{left:38px;top:736px;width:1118px;display:flex;justify-content:space-between}
.category{display:flex;gap:14px;width:260px}
.category svg{width:50px;height:56px;flex:none}
.category h3{font-weight:400;font-size:18px;letter-spacing:.5px;margin-top:4px}
.category p{font-family:Arial,sans-serif;font-size:11px;line-height:1.3;color:var(--muted);width:140px}
.rule{left:38px;width:1118px;height:1px;background:var(--rule)}

/* products */
.section-title{left:0;width:1200px;text-align:center;font-size:28px;letter-spacing:.5px;font-weight:400}
.tabs{left:0;width:1200px;top:958px;display:flex;justify-content:center;gap:20px;font-size:12px;letter-spacing:.5px}
.tabs span.active{border-bottom:2px solid var(--ink);padding-bottom:10px}
.products{left:60px;top:1070px;width:1080px;display:flex;justify-content:space-between}
.product{width:240px;position:relative;text-align:center}
.product-photo{height:160px;margin:0 16px;border-radius:50%;background:radial-gradient(ellipse at 50% 45%,var(--ring-a),var(--ring-b) 60%,transparent 72%)}
.save{position:absolute;right:10px;top:8px;text-align:right;font-size:18px;line-height:1}
.save small{display:block;font-size:11px;margin-top:2px}
.product h4{font-weight:400;font-size:18px;margin-top:32px;letter-spacing:.5px}
.product .price{font-size:19px;margin-top:12px}
.btn-solid{background:var(--black);color:var(--paper);font-size:13px;display:flex;align-items:center;justify-content:center;letter-spacing:.3px;width:156px;height:46px}
.product .btn-solid{margin:18px auto 0}
.arrow{top:1204px;width:14px;height:36px}
.browse-1{left:520px;top:1472px}

/* loose diamonds */
.subtitle{left:0;width:1200px;text-align:center;font-family:Arial,sans-serif;font-size:12px;top:1660px}
.shapes{left:38px;top:1718px;width:1118px;display:flex;justify-content:space-between}
.shape{width:104px;text-align:center}
.shape-tile{height:104px;background:radial-gradient(circle at 50% 50%,#3c3c3c 0,#1a1a1a 34%,var(--tile) 52%)}
.shape span{display:block;margin-top:14px;font-size:12px;letter-spacing:.5px}

/* promo */
.promo{left:38px;top:1890px;width:1118px;height:334px;background:linear-gradient(100deg,#e9e5e3 0,#d9cfca 22%,#3a3a3a 34%,#1c1c1c 60%,#2a2a2a 80%,#141414 100%)}
.promo-text{left:454px;top:1990px;width:380px;text-align:center;color:var(--paper)}
.promo-text .kicker{font-size:14px}
.promo-text h2{font-weight:400;font-size:29px;margin:6px 0 4px}
.promo-text p{font-size:14px;line-height:1.3}
.promo .btn-outline{left:526px;top:222px;width:156px;height:46px}

/* testimonial */
.quote-mark{font-size:72px;line-height:1;font-family:Georgia,serif}
.testimonial{left:280px;top:2350px;width:640px;text-align:center;font-family:Arial,sans-serif;font-size:12px;line-height:1.4}
.client{left:0;width:1200px;text-align:center;top:2406px;font-size:28px;letter-spacing:.5px}
.stars{left:0;width:1200px;text-align:center;top:2448px;color:var(--gold);font-size:16px;letter-spacing:2px}
.testimonial-dots{left:578px;top:2500px;color:var(--ink)}
.browse-2{left:520px;top:2542px}

/* footer */
.footer{left:38px;top:2640px;width:1118px;height:316px;background:var(--black);color:var(--paper)}
.footer h5{position:absolute;top:48px;font-weight:400;font-size:28px;letter-spacing:.5px}
.footer ul{position:absolute;top:100px;list-style:none;font-size:13px;line-height:17px}
.contact-list li{display:flex;gap:10px;align-items:flex-start}
.contact-list svg{width:11px;height:11px;margin-top:3px;flex:none}
.links-list{letter-spacing:1.5px}
.links-list li::before{content:"•";margin-right:8px}
.email{position:absolute;left:888px;top:104px;width:180px;height:30px;border:1px solid var(--paper);font-size:11px;padding:8px}
.subscribe{position:absolute;left:888px;top:142px;width:180px;height:28px;background:var(--paper);color:var(--ink);font-size:10px;display:flex;align-items:center;justify-content:center}
.social{position:absolute;left:888px;top:194px;display:flex;gap:18px}
.social i{width:10px;height:10px;border-radius:50%;background:var(--paper)}
.footer .frule{position:absolute;left:44px;top:232px;width:1024px;height:1px;background:#555}
.copyright{position:absolute;left:44px;top:258px;font-size:12px}
.payments{position:absolute;right:50px;top:252px;display:flex;gap:8px}
.payments i{width:34px;height:20px;background:#d8d8d8;border-radius:2px}
</style>
</head>
<body>

<header>
  <div class="abs brand">
    <span class="brand-mark"></span>
    <span class="brand-name">QUINTORA<small>JEWELLERS</small></span>
  </div>
  <div class="abs header-icons">
    <svg viewBox="0 0 18 18" fill="none" stroke="#111" stroke-width="2"><circle cx="7.5" cy="7.5" r="5"/><path d="M11.5 11.5 16 16"/></svg>
    <svg viewBox="0 0 18 18" fill="none" stroke="#111" stroke-width="1.8"><circle cx="9" cy="6" r="3.5"/><path d="M2.5 17c0-4 3-6 6.5-6s6.5 2 6.5 6"/></svg>
    <svg viewBox="0 0 18 18" fill="none" stroke="#111" stroke-width="1.8"><path d="M9 16 2.5 9.5A3.8 3.8 0 0 1 9 4a3.8 3.8 0 0 1 6.5 5.5Z"/></svg>
    <svg viewBox="0 0 18 18" fill="none" stroke="#111" stroke-width="1.8"><path d="M1 2h3l2 10h9l2-7H5"/><circle cx="7" cy="15.5" r="1.3"/><circle cx="14" cy="15.5" r="1.3"/></svg>
  </div>
  <nav class="abs main-nav">
    <a>DIAMONDS</a><a>ENGAGEMENT RINGS</a><a>WEDDING RINGS</a><a>JEWELLERY</a><a>EDUCATION</a><a>FAQ</a>
  </nav>
</header>

<section class="abs hero">
  <div class="abs hero-gems" role="img" aria-label="Photograph of sparkling loose cut diamonds on a dark reflective surface"></div>
  <div class="abs hero-frame"></div>
  <div class="abs hero-title">
    <div class="kicker">CERTIFIED</div>
    <div class="big">LOOSE DIMONDS</div>
    <div class="amp"><span>&amp;</span> JEWELLERY</div>
  </div>
  <a class="abs btn-outline">SHOP NOW</a>
  <div class="abs dots"><i></i><i class="on"></i><i></i></div>
</section>

<section class="abs categories">
  <div class="category">
    <svg viewBox="0 0 50 56" fill="none" stroke="#111" stroke-width="3"><circle cx="25" cy="36" r="17"/><path d="M18 12h14l-7 8Z" fill="#111"/></svg>
    <div><h3>ENGAGEMENT RINGS</h3><p>Lorem Ipsum is simply dummy text of the printing.</p></div>
  </div>
  <div class="category">
    <svg viewBox="0 0 50 56" fill="none" stroke="#111" stroke-width="3"><circle cx="17" cy="30" r="14"/><circle cx="33" cy="30" r="14"/></svg>
    <div><h3>WEDDING RINGS</h3><p>Lorem Ipsum is simply dummy text of the printing.</p></div>
  </div>
  <div class="category">
    <svg viewBox="0 0 50 56" fill="none" stroke="#111" stroke-width="2.5"><circle cx="25" cy="8" r="5"/><path d="M25 13v12"/><path d="M19 25h12l-3 28h-6Z" fill="#111"/></svg>
    <div><h3>DIAMOND EARRINGS</h3><p>Lorem Ipsum is simply dummy text of the printing.</p></div>
  </div>
  <div class="category">
    <svg viewBox="0 0 50 56" fill="none" stroke="#111" stroke-width="2.5"><path d="M4 6q21 26 42 0"/><path d="M25 22c-6-6-14 0-8 8l8 10 8-10c6-8-2-14-8-8Z" fill="#111"/></svg>
    <div><h3>DIAMOND PENDANTS</h3><p>Lorem Ipsum is simply dummy text of the printing.</p></div>
  </div>
</section>

<div class="abs rule" style="top:844px"></div>

<h2 class="abs section-title" style="top:900px">FEATURE PRODUCTS</h2>
<div class="abs tabs"><span class="active">ALL</span><span>LATESTS</span><span>BEST SELLER</span><span>DISCOUNTED</span><span>OTHER</span></div>

<svg class="abs arrow" style="left:24px" viewBox="0 0 14 36" fill="none" stroke="#aaa" stroke-width="1.5"><path d="M12 2 2 18l10 16"/></svg>
<svg class="abs arrow" style="left:1162px" viewBox="0 0 14 36" fill="none" stroke="#111" stroke-width="1.5"><path d="M2 2l10 16L2 34"/></svg>

<section class="abs products">
  <article class="product">
    <div class="product-photo" role="img" aria-label="Photograph of a white gold diamond engagement ring"></div>
    <div class="save">SAVE<small>50% OFF</small></div>
    <h4>PRODUCT NAME</h4><div class="price">$ 500.0</div><a class="btn-solid">SHOP NOW</a>
  </article>
  <article class="product">
    <div class="product-photo" role="img" aria-label="Photograph of a yellow gold halo diamond ring"></div>
    <div class="save">SAVE<small>50% OFF</small></div>
    <h4>PRODUCT NAME</h4><div class="price">$ 500.0</div><a class="btn-solid">SHOP NOW</a>
  </article>
  <article class="product">
    <div class="product-photo" role="img" aria-label="Photograph of an oval halo diamond ring"></div>
    <div class="save">SAVE<small>50% OFF</small></div>
    <h4>PRODUCT NAME</h4><div class="price">$ 500.0</div><a class="btn-solid">SHOP NOW</a>
  </article>
  <article class="product">
    <div class="product-photo" role="img" aria-label="Photograph of a white gold diamond engagement ring"></div>
    <div class="save">SAVE<small>50% OFF</small></div>
    <h4>PRODUCT NAME</h4><div class="price">$ 500.0</div><a class="btn-solid">SHOP NOW</a>
  </article>
</section>

<a class="abs btn-solid browse-1">BROWS MORE</a>

<div class="abs rule" style="top:1570px"></div>

<h2 class="abs section-title" style="top:1616px">LOOSE DIAMONDS</h2>
<div class="abs subtitle">Brows by shape</div>

<section class="abs shapes">
  <div class="shape"><div class="shape-tile" role="img" aria-label="Line drawing of a round cut diamond"></div><span>ROUND</span></div>
  <div class="shape"><div class="shape-tile" role="img" aria-label="Line drawing of a princess cut diamond"></div><span>PRINCESS</span></div>
  <div class="shape"><div class="shape-tile" role="img" aria-label="Line drawing of a marquise cut diamond"></div><span>MARQUISE</span></div>
  <div class="shape"><div class="shape-tile" role="img" aria-label="Line drawing of an emerald cut diamond"></div><span>EMERALD</span></div>
  <div class="shape"><div class="shape-tile" role="img" aria-label="Line drawing of a pear cut diamond"></div><span>PEAR</span></div>
  <div class="shape"><div class="shape-tile" role="img" aria-label="Line drawing of an oval cut diamond"></div><span>OVAL</span></div>
  <div class="shape"><div class="shape-tile" role="img" aria-label="Line drawing of a heart cut diamond"></div><span>HEART</span></div>
  <div class="shape"><div class="shape-tile" role="img" aria-label="Line drawing of a radiant cut diamond"></div><span>REDIANT</span></div>
  <div class="shape"><div class="shape-tile" role="img" aria-label="Line drawing of an asscher cut diamond"></div><span>ASCHER</span></div>
  <div class="shape"><div class="shape-tile" role="img" aria-label="Line drawing of a cushion cut diamond"></div><span>CUSHION</span></div>
</section>

<section class="abs promo" role="img" aria-label="Photograph of a hand wearing a marquise diamond ring beside a ring in an open gift box on dark satin">
  <a class="abs btn-outline">SHOP NOW</a>
</section>
<div class="abs promo-text">
  <div class="kicker">We Guarantee The</div>
  <h2>Lowest Prices In The World</h2>
  <p>If You Happen To Find A Price Cheaper Than Ours, We Will Beat It</p>
</div>

<h2 class="abs section-title" style="top:2284px">OUR CLIENTS SAY`S</h2>
<div class="abs quote-mark" style="left:250px;top:2336px">&ldquo;</div>
<p class="abs testimonial">Lorem Ipsum is simply dummy text of the printing and typesetting industry. Lorem Ipsum has been the industry's standard dummy text ever since the 1500s.</p>
<div class="abs quote-mark" style="left:914px;top:2346px">&rdquo;</div>
<div class="abs client">MARA ELLISON</div>
<div class="abs stars">★★★★★</div>
<div class="abs dots testimonial-dots"><i></i><i class="on"></i><i></i></div>
<a class="abs btn-solid browse-2">BROWS MORE</a>

<footer class="abs footer">
  <h5 style="left:44px">CONTACT</h5>
  <ul class="contact-list" style="left:44px">
    <li><svg viewBox="0 0 12 12" fill="#fff"><path d="M2 1h3l1 3-2 1a6 6 0 0 0 3 3l1-2 3 1v3c-6 1-10-3-9-9Z"/></svg>(+012) 555 0142</li>
    <li><svg viewBox="0 0 12 12" fill="#fff"><path d="M2 1h3l1 3-2 1a6 6 0 0 0 3 3l1-2 3 1v3c-6 1-10-3-9-9Z"/></svg>(+012) 555 0142</li>
    <li><svg viewBox="0 0 12 12" fill="#fff"><path d="M2 1h3l1 3-2 1a6 6 0 0 0 3 3l1-2 3 1v3c-6 1-10-3-9-9Z"/></svg>(+012) 555 0142</li>
    <li><svg viewBox="0 0 12 12" fill="#fff"><path d="M1 3h10v7H1Z"/><path d="m1 3 5 4 5-4" stroke="#000" fill="none"/></svg>info@quintorajewellers.example</li>
    <li><svg viewBox="0 0 12 12" fill="#fff"><path d="M6 11S2 7 2 4.5a4 4 0 0 1 8 0C10 7 6 11 6 11Z"/></svg>18 Larkspur Lane<br>Hollis, MA 02990</li>
  </ul>
  <h5 style="left:362px">QUICK LINK</h5>
  <ul class="links-list" style="left:362px">
    <li>DIAMONDS</li><li>ENGAGEMENT RINGS</li><li>WEDDING RINGS</li><li>JEWELLERY</li><li>EDUCATION</li><li>FAQ</li>
  </ul>
  <h5 style="left:630px">TIMING</h5>
  <ul style="left:630px">
    <li>Mon : 9:00 am – 5:30 pm</li><li>Tue : 9:00 am – 5:30 pm</li><li>Wed : 9:00 am – 5:30 pm</li><li>Thu : 9:00 am – 9:00 pm</li><li>Fri : 9:00 am – 9:00 pm</li><li>Sat : 9:00 am – 5:00 pm</li><li>Sun : 10:00 am – 5:00 pm</li>
  </ul>
  <h5 style="left:888px">NEWSLETTER</h5>
  <div class="email">Email</div>
  <div class="subscribe">SUBSCRIBE NOW</div>
  <div class="social"><i></i><i></i><i></i><i></i><i></i><i></i></div>
  <div class="frule"></div>
  <div class="copyright">Copyright © 2017 Quintora Jewellers - All Rights Reserved.</div>
  <div class="payments"><i></i><i></i><i></i><i></i><i></i></div>
</footer>

</body>
</html>
```